Design the most beautiful 'value book' for our team

We have a book that describes the value of the team. Each value is illustrated through stories told by the team members (5 to 6 per value).
The purpose of the 'value book' is for every new team members to read it and be inspired by it. It's also a reference of existing team members.
The value book will be displayed in public areas in the company. Any employees from other teams can pick it up and read it, and hopefully embrace the values described in the book.

We would like the value book to have a professional, minimalist design with fresh colors. When people pick it up, we want them to feel curious and think 'what is this magazine?' and when they open it, we want them to go through each pages because they are so beautiful by design.

An excerpt of the book is enclosed (book preface + first value)

Font styles to use
Serif
Sans Serif

Requirements
Must have
• Attractive cover
• Consistent theme throughout the book
• Design allows to easily add more stories as time goes by
• Pagination
• Table of content
Should not have
• No stock photos / images (ok to use graphics and other visuals)

```html
<!DOCTYPE html>
<html lang="en">
<head>
<meta charset="utf-8">
<title>The Nova Value Book</title>
<link rel="stylesheet" href="https://fonts.googleapis.com/css2?family=Saira+Condensed:wght@300;400&family=Saira+Extra+Condensed:wght@400;500&family=Open+Sans:wght@600;700&display=swap">
<style>
:root{
  --backdrop:#e4e5e7;
  --paper:#ebe2d0;
  --paper-edge:#d8c9ab;
  --ink:#1d2336;
  --title-navy:#1f2a4a;
  --accent-pink:#e8a6a6;
  --mist:#f1e7e4;
  --forest-mid:#3f6456;
  --forest-dark:#1a2e28;
  --cover-type:#f4e8e6;
  --panel-grey:#8d8781;
  --panel-line:#f4f1ec;
  --folio-bg:#ffffff;
}
*{margin:0;padding:0;box-sizing:border-box}
html,body{width:798px;height:1200px;overflow:hidden;background:var(--backdrop)}
.canvas{position:relative;width:798px;height:1200px}
.spread{position:absolute;left:49px;width:700px;height:500px;display:flex;box-shadow:0 10px 24px rgba(0,0,0,.18)}
.spread--cover{top:40px}
.spread--inside{top:620px}
.page{position:relative;width:350px;height:500px;overflow:hidden}

/* cover */
.cover-photo{position:absolute;inset:0;background:linear-gradient(180deg,var(--mist) 0%,#dcd9d3 30%,var(--forest-mid) 62%,var(--forest-dark) 100%)}
.cover-feature{position:absolute;left:40px;top:0;width:310px;height:300px;background:radial-gradient(ellipse at 55% 35%,#f6d2c4 0%,#c9a79c 30%,rgba(120,130,125,.55) 60%,rgba(90,110,100,0) 80%)}
.cover-title{position:absolute;right:36px;top:282px;width:240px;text-align:center;font-family:"Saira Condensed",sans-serif;font-weight:300;color:var(--cover-type);font-size:46px;line-height:.98;letter-spacing:1px;text-transform:uppercase}
.cover-author{position:absolute;right:30px;top:428px;width:240px;text-align:center;font-family:"Saira Condensed",sans-serif;font-weight:300;color:var(--cover-type);font-size:12px;letter-spacing:9px;text-transform:uppercase}
.spine{position:absolute;left:349px;top:0;width:2px;height:500px;background:rgba(0,0,0,.12)}

/* inside */
.page--inside{background:radial-gradient(ellipse at 50% 45%,var(--paper) 55%,var(--paper-edge) 100%)}
.heading{position:absolute;font-family:"Saira Extra Condensed",sans-serif;font-weight:500;color:var(--title-navy);font-size:30px;line-height:.95}
.heading .soft{color:var(--accent-pink);font-weight:400}
.body{position:absolute;font-family:"Open Sans",sans-serif;font-weight:600;color:var(--ink);font-size:6px;line-height:1.28}
.body p{margin-bottom:4px}
.sketch{position:absolute;border-radius:4px}
.folio{position:absolute;bottom:14px;width:18px;height:18px;border-radius:50%;background:var(--folio-bg);font-family:"Open Sans",sans-serif;font-weight:700;font-size:6px;color:var(--ink);display:flex;align-items:center;justify-content:center}
.folio-rule{position:absolute;bottom:22px;height:1px;background:var(--folio-bg)}
.values-panel{position:absolute;left:128px;top:340px;width:200px;height:130px;background:var(--panel-grey);opacity:.92}
.value{position:absolute;width:70px;text-align:center;font-family:"Open Sans",sans-serif;font-weight:600;font-size:5.5px;color:var(--panel-line);text-transform:uppercase}
.value svg{display:block;margin:0 auto 2px;stroke:var(--panel-line);fill:none;stroke-width:1.2}
.gutter-shade{position:absolute;top:0;width:20px;height:500px}
</style>
</head>
<body>
<main class="canvas">

  <section class="spread spread--cover">
    <div class="page page--back">
      <div class="cover-photo" role="img" aria-label="Misty pine forest photograph"></div>
    </div>
    <div class="page page--front">
      <div class="cover-photo" role="img" aria-label="Misty pine forest continuing across the front cover"></div>
      <div class="cover-feature" role="img" aria-label="Glowing brain with a bare tree held in open hands"></div>
      <h1 class="cover-title">The<br>Nova Value<br>Book</h1>
      <p class="cover-author">Author Name</p>
    </div>
    <div class="spine"></div>
  </section>

  <section class="spread spread--inside">
    <div class="page page--inside">
      <h2 class="heading" style="left:22px;top:24px">Why did we write<br>this book ?</h2>
      <div class="sketch" style="left:215px;top:84px;width:100px;height:50px;background:radial-gradient(ellipse,#6d6558 0%,rgba(109,101,88,0) 70%)" role="img" aria-label="Pencil sketch of a hand writing with a pen"></div>
      <div class="body" style="left:22px;top:84px;width:165px">
        <p>Every company has a vision, a set of values and a unique culture.<br>Every team should have its own vision, its own set of values and its own culture.<br>Both things aren't necessarily exactly the same.<br>However they must be in alignment.</p>
        <p>We believe that values are what makes the identity of a team.<br>Identity gives you a sense of pride, safety and belonging.<br>It also gives you a strong foundation from which to grow and become more.</p>
        <p>Without an identity, a team is just a group of people trying to lay bricks individually.<br>With an identity, a team can build a cathedral.</p>
        <p>By reflecting on what is the most important in a team, you establish a sense of clarity.<br>And only with clarity can you navigate in this chaotic working environment.</p>
        <p>In 'easy' time, our values carry us in places we didn't know we could go.<br>When the difficult times arise, we rely on our values to make key decisions.</p>
        <p>Such decisions include how to behave and not behave.<br>Who to hire and who to let go of.<br>What to tolerate and to what extent.<br>In which activities to engage in and be focused on.<br>And which activities to let other teams handle.</p>
      </div>
      <div class="body" style="left:198px;top:140px;width:130px">
        <p>This book was written by the NOVA team members.<br>It describes our identity, who we are.</p>
        <p>We hope this book will be a source of inspiration for you.</p>
        <p>In any case, we highly recommend you to reflect upon it.</p>
        <p>What's your true identity?</p>
        <p>Feel free to reach out to any of the NOVA team members for further discussion.</p>
      </div>
      <div class="sketch" style="left:130px;top:360px;width:200px;height:140px;background:radial-gradient(ellipse at 55% 60%,#7a3436 0%,#a86a6a 35%,rgba(232,166,166,.35) 60%,rgba(235,226,208,0) 80%)" role="img" aria-label="Photograph of a person in a knit hat seen from behind"></div>
      <div class="folio-rule" style="left:40px;width:290px"></div>
      <div class="folio" style="left:22px">01</div>
      <div class="gutter-shade" style="right:0;background:linear-gradient(90deg,rgba(0,0,0,0),rgba(0,0,0,.1))"></div>
    </div>

    <div class="page page--inside">
      <h2 class="heading" style="left:24px;top:100px">How is <span class="soft">this book</span><br>organized?</h2>
      <div class="sketch" style="left:175px;top:120px;width:175px;height:210px;background:radial-gradient(ellipse at 55% 40%,rgba(226,140,140,.55) 0%,rgba(200,170,160,.35) 45%,rgba(235,226,208,0) 75%)" role="img" aria-label="Faded illustration of a bare tree in pink tones"></div>
      <div class="body" style="left:24px;top:170px;width:150px">
        <p>We could have compiled a shortlist of what we value the most and give it to you.<br>But you wouldn't read it, because it'd be so boring and meaningless.</p>
        <p>Instead we took some time to reflect on our core values, and why.<br>This lead us to share a variety of stories.</p>
        <p>You will find in this book a series of story from each team members.<br>Each story illustrates a core value.</p>
      </div>
      <div class="body" style="left:140px;top:308px;width:190px">
        <p>To make it easier for you to navigate in this book, here are our 6 team values (in no particular order):</p>
      </div>
      <div class="sketch" style="left:0;top:350px;width:140px;height:150px;background:radial-gradient(ellipse at 45% 50%,#8a8781 0%,#b5b0a7 40%,rgba(235,226,208,0) 75%)" role="img" aria-label="Black and white photograph of a group of children"></div>
      <div class="values-panel">
        <div class="value" style="left:14px;top:10px"><svg width="22" height="18" viewBox="0 0 22 18"><path d="M2 16h18M4 14l5-5 4 3 6-7M15 5h4v4"/></svg>Growth</div>
        <div class="value" style="left:114px;top:10px"><svg width="20" height="18" viewBox="0 0 20 18"><path d="M10 2l7 4v7l-7 4-7-4V6zM3 6l7 4 7-4M10 10v7"/></svg>Contribution</div>
        <div class="value" style="left:14px;top:50px"><svg width="18" height="18" viewBox="0 0 18 18"><path d="M4 2h8l3 3v11H4zM6 7h7M6 10h7M6 13h5"/></svg>Result oriented</div>
        <div class="value" style="left:114px;top:50px"><svg width="22" height="18" viewBox="0 0 22 18"><path d="M2 8l5-4 4 3 4-3 5 4M5 10l4 4 4-3 4 3 3-4"/></svg>Understanding</div>
        <div class="value" style="left:14px;top:90px"><svg width="18" height="18" viewBox="0 0 18 18"><circle cx="9" cy="9" r="6"/><circle cx="9" cy="9" r="2"/><circle cx="9" cy="3" r="1.5"/><circle cx="15" cy="9" r="1.5"/><circle cx="3" cy="9" r="1.5"/></svg>Innovation</div>
        <div class="value" style="left:114px;top:90px"><svg width="20" height="18" viewBox="0 0 20 18"><path d="M10 17V9M10 9L4 3M10 9l6-6M10 9V2M4 3h3M4 3v3M16 3h-3M16 3v3M8 4l2-2 2 2"/></svg>Flexibility</div>
      </div>
      <div class="body" style="left:110px;top:470px;width:150px;font-weight:700">
        <p>We wish you to enjoy this book.<br>If it inspires you, spread the word!</p>
      </div>
      <div class="folio-rule" style="left:20px;width:290px"></div>
      <div class="folio" style="right:22px">02</div>
      <div class="gutter-shade" style="left:0;background:linear-gradient(90deg,rgba(0,0,0,.1),rgba(0,0,0,0))"></div>
    </div>
  </section>

</main>
</body>
</html>
```